Etikett für Honigunternehmen gesucht
Zielgruppe
Wir produzieren Honig, möchten aber in naher Zukunft auch andere Honigprodukte produzieren (Cremen, Wein, Likör......). Unsere Zielgruppe sind alle.
Aufgabenstellung
Wir wünschen uns Schlichtheit und Einfachheit. Wichtig ist uns auch, dass das Design modern wirkt. Es soll kein typisches Honigetikett mit 'Wiesen und Bienen' werden. Das Glas wird auch schlicht und modern werden. Es wird nur 250-g- und 500-g-Gläser geben. Die Gewichtsangabe muss sichtbar und mind. 4 mm groß sein. Name, Anschrift und Telefonnummer können auch am Deckel oder ganz klein und leserlich am unteren Etikettenrand stehen. Dabei ist zu beachten, dass der kleinste Buchstabe min. 1,2 mm groß ist.
Etiketten-Design für Honigglas Etiketten-Design für Honigglas"
Format: Etikett für 250-gr.-Honigglas (TO ∅ 63 mm). Standardmaßgrösse 165 × 40 mm Design: schlicht, hochwertig, modern, edel/royal, unkonventionelles Design (weg von Bienen, Waben, Landschaften usw.), dunkle Farbtöne in Kontrast zu heller Schrift, die beiden Textbausteine 'Los Nr. ' sowi..
Attraktives Etiketten-Design für Honig Attraktives Etiketten-Design für Honig"
Wir verkaufen zur Zeit vor allem Waldhonig, streben aber auch einen Blütenhonig an. Das Etikett soll daher entweder den Wald wiederspiegeln oder aber neutral sein, so dass der Schriftzug Waldhonig oder Blütenhonig jeweils eingesetzt werden kann. Wichtig ist mir der Ortszusatz 'aus dem Glottertal..
Etiketten-Design für Produkte eines Familienbetriebs mit Imkerei und Hühnerhaltung Etiketten-Design für Produkte eines Familienbetriebs mit Imkerei und Hühnerhaltung"
1. Zentrale, auf allen Etiketten wiederkehrende Elemente: - Unser Riegelhaus (stilisiert) (Bild beiliegend) - Das Wort 'Marlock' (Anmerkung: ohne Anführungszeichen) - die zentralen Elemente sollen die Produkte nicht überragen. 2. Dezente Adresse: - Familie Obrecht, Talbrunn, CH-9388 Forlenz 3...
Etiketten-Design für Kurkuma-Honig Etiketten-Design für Kurkuma-Honig"
Etikett für 500g // Stanze eckig (210x35mm), Druckdatei entsprechend Vorgaben https://etikettwerk-muster.de/faq/ Vorgaben für das Grünquell Logo im Anhang Vorgaben für EG Öko Logo : https://example-oekoamt.eu/landbau/bio/download/logo_de Pflichtangaben auf dem Etikett: Gewicht, Adresse siehe Beispiel..
Etiketten-Design für Blütenhonig und Waldhonig gesucht Etiketten-Design für Blütenhonig und Waldhonig gesucht"
Zwei verschiedene Etiketten-Desings 1 x Blütenhonig sowie 1 x Waldhonig für unterschiedliche Honigglasgrößen (500 g und 250 g) Die Maße für die Etiketten wären: Für 500-Gramm-Glas 210 mm x 45 mm für's 250-Gramm-Glas 180 mm x 38 mm. Wir sind auch offen für neue Vorschläge bezüglich ..

```html
<!DOCTYPE html>
<html lang="de">
<head>
<meta charset="utf-8">
<title>Honig Etiketten – Sortenreihe</title>
<link rel="stylesheet" href="https://fonts.googleapis.com/css2?family=Fira+Sans:ital,wght@0,400;0,600;1,700&display=swap">
<style>
  :root {
    --page: #ffffff;
    --panel: #8c4b2d;
    --panel-light: #9a5533;
    --gold: #d8a21e;
    --gold-text: #d9ad12;
    --white: #ffffff;
    --peach: #f9bd8a;
    --mint: #c6e0a0;
    --rose: #f4b1b0;
    --sage: #8bbb9a;
    --apricot: #fdd08e;
    --bee-tone: #3a2a1c;
  }
  * { margin: 0; padding: 0; box-sizing: border-box; }
  html, body { width: 848px; height: 1200px; overflow: hidden; background: var(--page); }
  body { position: relative; font-family: "Fira Sans", Arial, sans-serif; }

  .label {
    position: absolute;
    width: 503px;
    height: 370px;
    transform-origin: 0 0;
  }
  .label--hero { left: 179px; top: 248px; }
  .label--small { transform: scale(.45); top: 918px; }
  .label--acacia { left: 36px; }
  .label--summer { left: 222px; }
  .label--forest { left: 409px; }
  .label--comb { left: 598px; }

  .label__side {
    position: absolute;
    top: 62px;
    width: 114px;
    height: 285px;
    background: var(--side, var(--peach));
  }
  .label__side--left { left: 0; }
  .label__side--right { right: 0; }

  .label__panel {
    position: absolute;
    left: 114px;
    top: 58px;
    width: 275px;
    height: 312px;
    background: linear-gradient(180deg, var(--panel) 0%, var(--panel-light) 55%, var(--panel) 100%);
    text-align: center;
    color: var(--white);
  }

  .label__emblem {
    position: absolute;
    left: 176px;
    top: 0;
    width: 150px;
    height: 130px;
  }

  .label__variety {
    position: absolute;
    left: 0; right: 0;
    top: 108px;
    font-weight: 600;
    font-size: 26px;
    line-height: 1;
    letter-spacing: .5px;
  }
  .label__product {
    position: absolute;
    left: 0; right: 0;
    top: 133px;
    font-weight: 400;
    font-size: 62px;
    line-height: 1;
    font-variant: small-caps;
    letter-spacing: 1px;
  }
  .label__producer {
    position: absolute;
    left: 0; right: 0;
    top: 194px;
    font-weight: 700;
    font-style: italic;
    font-size: 30px;
    line-height: 1;
    font-variant: small-caps;
    letter-spacing: 2px;
    color: var(--gold-text);
  }

  .label__band {
    position: absolute;
    left: 0; right: 0; bottom: 4px;
    height: 27px;
    background: var(--gold);
    display: flex;
    justify-content: space-between;
    align-items: center;
    padding: 0 6px;
    font-weight: 600;
    font-size: 30px;
    line-height: 1;
    letter-spacing: 3px;
    color: var(--white);
  }
  .label__band span { position: relative; top: 5px; }

  .label__bee {
    position: absolute;
    left: 112px;
    bottom: 8px;
    width: 52px;
    height: 44px;
    border-radius: 40%;
    background: linear-gradient(135deg, #5a3a22, var(--bee-tone));
  }
</style>
</head>
<body>

  <!-- Hauptetikett -->
  <section class="label label--hero" style="--side: var(--peach)">
    <div class="label__side label__side--left"></div>
    <div class="label__side label__side--right"></div>
    <div class="label__panel">
      <p class="label__variety">FRÜHLINGSBLÜTEN</p>
      <p class="label__product">Honig</p>
      <p class="label__producer">Konrad Wendlinger</p>
      <div class="label__band"><span>****</span><span>****</span></div>
      <div class="label__bee" role="img" aria-label="Illustration einer Biene"></div>
    </div>
    <svg class="label__emblem" viewBox="0 0 150 130">
      <polygon points="37.5,3 112.5,3 147,65 112.5,127 37.5,127 3,65" fill="#fff" stroke="#d8a21e" stroke-width="6"/>
      <polygon points="55,35 95,35 113,65 95,95 55,95 37,65" fill="#c9a48c" role="img" aria-label="Sortensymbol: farbige Blütenblätter"/>
    </svg>
  </section>

  <!-- Sortenreihe -->
  <section class="label label--small label--acacia" style="--side: var(--mint)">
    <div class="label__side label__side--left"></div>
    <div class="label__side label__side--right"></div>
    <div class="label__panel">
      <p class="label__variety">BLÜTEN- /AKAZIEN-</p>
      <p class="label__product">Honig</p>
      <p class="label__producer">Konrad Wendlinger</p>
      <div class="label__band"><span>****</span><span>****</span></div>
      <div class="label__bee" role="img" aria-label="Illustration einer Biene"></div>
    </div>
    <svg class="label__emblem" viewBox="0 0 150 130">
      <polygon points="37.5,3 112.5,3 147,65 112.5,127 37.5,127 3,65" fill="#fff" stroke="#d8a21e" stroke-width="6"/>
      <polygon points="55,35 95,35 113,65 95,95 55,95 37,65" fill="#8cc63f" role="img" aria-label="Sortensymbol: grüner Zweig"/>
    </svg>
  </section>

  <section class="label label--small label--summer" style="--side: var(--rose)">
    <div class="label__side label__side--left"></div>
    <div class="label__side label__side--right"></div>
    <div class="label__panel">
      <p class="label__variety">SOMMERBLÜTEN</p>
      <p class="label__product">Honig</p>
      <p class="label__producer">Konrad Wendlinger</p>
      <div class="label__band"><span>****</span><span>****</span></div>
      <div class="label__bee" role="img" aria-label="Illustration einer Biene"></div>
    </div>
    <svg class="label__emblem" viewBox="0 0 150 130">
      <polygon points="37.5,3 112.5,3 147,65 112.5,127 37.5,127 3,65" fill="#fff" stroke="#d8a21e" stroke-width="6"/>
      <polygon points="55,35 95,35 113,65 95,95 55,95 37,65" fill="#e0306f" role="img" aria-label="Sortensymbol: pinke Blüte"/>
    </svg>
  </section>

  <section class="label label--small label--forest" style="--side: var(--sage)">
    <div class="label__side label__side--left"></div>
    <div class="label__side label__side--right"></div>
    <div class="label__panel">
      <p class="label__variety">WALD- UND BLÜTEN-</p>
      <p class="label__product">Honig</p>
      <p class="label__producer">Konrad Wendlinger</p>
      <div class="label__band"><span>****</span><span>****</span></div>
      <div class="label__bee" role="img" aria-label="Illustration einer Biene"></div>
    </div>
    <svg class="label__emblem" viewBox="0 0 150 130">
      <polygon points="37.5,3 112.5,3 147,65 112.5,127 37.5,127 3,65" fill="#fff" stroke="#d8a21e" stroke-width="6"/>
      <polygon points="55,35 95,35 113,65 95,95 55,95 37,65" fill="#1f6b3a" role="img" aria-label="Sortensymbol: Tanne"/>
    </svg>
  </section>

  <section class="label label--small label--comb" style="--side: var(--apricot)">
    <div class="label__side label__side--left"></div>
    <div class="label__side label__side--right"></div>
    <div class="label__panel">
      <p class="label__variety">WABEN-</p>
      <p class="label__product">Honig</p>
      <div class="label__band"><span>****</span><span>****</span></div>
      <div class="label__bee" role="img" aria-label="Illustration einer Biene"></div>
    </div>
    <svg class="label__emblem" viewBox="0 0 150 130">
      <polygon points="37.5,3 112.5,3 147,65 112.5,127 37.5,127 3,65" fill="#fff" stroke="#d8a21e" stroke-width="6"/>
      <polygon points="58,45 92,45 108,65 92,85 58,85 42,65" fill="#d6b400"/>
    </svg>
  </section>

</body>
</html>
```